BRPS Postcard Design: Mosquito Control, Lawn Maintenance and Pressure washing

I have a new company based in Atlanta,Georgia named Brookvale Pest Shield Services, LLC. We specializes in Mosquito Control. We also have additional services: Lawn maintenance, Pressure Washing and Gutter Cleaning. I would like to see designs with the colors Black, Red, Gray. We would like the customer to think of us when it comes to Enjoying a mosquito free yard and improving the look and feel of their home and lawn.

Industry/Entity Type

It Company

Requirements
Nice to have
• Treatment plans starting at $69/mt - front of card
• The additional services we offer - back of card.

```html
<!DOCTYPE html>
<html lang="en">
<head>
<meta charset="utf-8">
<title>BRPS Postcard – Additional Services</title>
<link rel="stylesheet" href="https://fonts.googleapis.com/css2?family=Fredoka:wght@600&family=Roboto:wght@400;700&display=swap">
<style>
  :root {
    --black: #000000;
    --ink: #1a1a1a;
    --red: #b3101a;
    --red-dark: #7a0f14;
    --bar-red: #8e1418;
    --pill: #3a3a3a;
    --white: #ffffff;
    --gray-dark: #6f6f6f;
    --gray-mid: #a9a9a9;
    --gray-light: #dcdcdc;
    --line: #8a7a66;
  }
  * { box-sizing: border-box; margin: 0; padding: 0; }
  html, body { width: 1200px; height: 779px; overflow: hidden; background: var(--white); }
  .postcard {
    position: relative; width: 1200px; height: 779px; overflow: hidden;
    background: var(--black);
    font-family: "Roboto", Arial, sans-serif;
  }
  .mailing-side {
    position: absolute; left: 686px; top: 0; width: 514px; height: 779px;
    background: linear-gradient(90deg, var(--gray-dark) 0%, var(--gray-mid) 35%, var(--gray-light) 100%);
  }
  .services-title {
    position: absolute; left: 23px; top: 15px; width: 427px; height: 109px;
    background: var(--pill); border: 5px solid var(--red-dark); border-radius: 50px;
    color: var(--white); font-family: "Fredoka", Arial, sans-serif; font-weight: 600;
    font-size: 40px; line-height: 44px; text-align: center;
    display: flex; align-items: center; justify-content: center;
  }
  .service-bar {
    position: absolute; left: 23px; width: 431px; height: 56px;
    background: var(--bar-red); border-radius: 28px 0 0 28px;
    color: var(--white); font-size: 31px; letter-spacing: 0.5px;
    display: flex; align-items: center; padding-left: 34px;
  }
  .service-bar.lawn { top: 170px; }
  .service-bar.washing { top: 354px; }
  .service-bar.gutter { top: 543px; }
  .service-icon {
    position: absolute; left: 429px; width: 228px; height: 158px;
    border: 9px solid var(--red-dark); border-radius: 80px; background: var(--white);
    overflow: hidden; display: flex; align-items: center; justify-content: center;
  }
  .service-icon.lawn { top: 116px; }
  .service-icon.washing { top: 305px; }
  .service-icon.gutter { top: 493px; }
  .icon-art { width: 150px; height: 110px; border-radius: 30px; }
  .lawn .icon-art { background: linear-gradient(#2a2a2a 55%, #2e8b3a 55%); }
  .washing .icon-art { background: linear-gradient(90deg, #5a3315, #7a4a22); }
  .gutter .icon-art { background: linear-gradient(135deg, #d0202a 50%, #6a6aa8 50%); }
  .brand-block {
    position: absolute; left: 60px; top: 662px; width: 330px; text-align: center;
    color: var(--red);
  }
  .brand-name { font-weight: 700; font-size: 21px; line-height: 26px; }
  .brand-phone { font-weight: 700; font-size: 24px; margin-top: 6px; }
  .mark {
    position: absolute; left: 722px; top: 36px; width: 186px; height: 186px;
    display: flex; align-items: center; justify-content: center; gap: 8px;
  }
  .mark-dot { width: 24px; height: 24px; border-radius: 50%; background: var(--red); flex: none; }
  .mark-name { font-family: "Roboto", Arial, sans-serif; font-weight: 700; font-size: 34px; color: var(--red); }
  .stamp-box {
    position: absolute; left: 1001px; top: 35px; width: 154px; height: 149px;
    background: var(--white); color: #777; font-size: 17px;
    display: flex; align-items: center; justify-content: center;
  }
  .address-box {
    position: absolute; left: 736px; top: 325px; width: 446px; height: 309px;
    background: #b5b5b5; border: 1px solid #c8c8c8;
  }
  .address-line { position: absolute; left: 37px; width: 382px; height: 2px; background: var(--line); }
  .barcode-area {
    position: absolute; left: 504px; top: 669px; width: 679px; height: 100px;
    background: var(--white); color: var(--ink); font-size: 27px;
    display: flex; align-items: center; justify-content: center;
  }
</style>
</head>
<body>
<main class="postcard">
  <section class="mailing-side"></section>

  <h1 class="services-title">The Additional<br>Services We OFFER</h1>

  <div class="service-bar lawn">LAWN MAINTANANCE</div>
  <div class="service-icon lawn"><div class="icon-art" role="img" aria-label="Illustration of a push lawn mower on grass"></div></div>

  <div class="service-bar washing">PRESSURE WASHING</div>
  <div class="service-icon washing"><div class="icon-art" role="img" aria-label="Illustration of a pressure washer wand cleaning a wooden fence"></div></div>

  <div class="service-bar gutter">GUTTER CLEANING</div>
  <div class="service-icon gutter"><div class="icon-art" role="img" aria-label="Illustration of a bucket, dustpan and cleaning supplies"></div></div>

  <div class="brand-block">
    <p class="brand-name">Brookvale Pest Shield Services, LLC</p>
    <p class="brand-phone">404-555-0182</p>
  </div>

  <div class="mark"><span class="mark-dot"></span><span class="mark-name">BRPS</span></div>

  <div class="stamp-box">STAMP</div>

  <div class="address-box">
    <span class="address-line" style="top:60px"></span>
    <span class="address-line" style="top:124px"></span>
    <span class="address-line" style="top:188px"></span>
    <span class="address-line" style="top:250px"></span>
  </div>

  <div class="barcode-area">Barcode Area</div>
</main>
</body>
</html>
```